business card design for luxurious real estate brand

using the attached logo, i am looking for a 2-sided business card design. the back should be the gold logo on black background. the front needs to include: gold logo, name, phone, email, and website

Industry/Entity Type

real estate

Contact Information for Business Card

logo, name, email, phone, website

Font styles to use
Sans Serif

```html
<!DOCTYPE html>
<html lang="en">
<head>
<meta charset="utf-8">
<title>Casa Lumen — Business Card</title>
<link rel="stylesheet" href="https://fonts.googleapis.com/css2?family=Poppins:wght@400;500;600&display=swap">
<style>
  :root {
    --backdrop: #c9c9c9;
    --card-black: #0e0e0e;
    --card-graphite: #2a2a2a;
    --card-white: #ffffff;
    --gold: #f7c600;
    --ink: #1a1a1a;
    --text-light: #f2f2f2;
  }
  * { margin: 0; padding: 0; box-sizing: border-box; }
  html, body {
    width: 1200px; height: 2214px; overflow: hidden;
    background: var(--backdrop);
    font-family: "Poppins", sans-serif;
  }
  .canvas { position: relative; width: 1200px; height: 2214px; }
  .card {
    position: absolute; left: 150px; width: 900px; height: 530px;
    overflow: hidden;
    box-shadow: 14px 18px 26px rgba(0,0,0,0.35);
  }
  .card--front { top: 420px; }
  .card--back { top: 1260px; background: var(--card-black); }
  .card__shapes { position: absolute; inset: 0; width: 100%; height: 100%; }

  .brand { position: absolute; display: flex; align-items: center; gap: 18px; }
  .brand__square { background: var(--gold); }
  .brand__name { font-weight: 500; letter-spacing: 0.12em; white-space: nowrap; }

  .card--front .brand { left: 64px; top: 190px; }
  .card--front .brand__square { width: 30px; height: 30px; }
  .card--front .brand__name { font-size: 34px; color: var(--ink); }

  .card--back .brand { left: 0; right: 0; top: 240px; justify-content: center; }
  .card--back .brand__square { width: 40px; height: 40px; }
  .card--back .brand__name { font-size: 48px; color: var(--gold); }

  .holder { position: absolute; left: 525px; top: 150px; }
  .holder__name { font-size: 46px; font-weight: 500; color: var(--text-light); line-height: 1.1; }
  .holder__role { font-size: 20px; letter-spacing: 0.16em; color: var(--gold); margin-top: 6px; }

  .contacts { position: absolute; left: 470px; top: 350px; list-style: none; }
  .contacts__item {
    display: flex; align-items: center; gap: 14px;
    font-size: 23px; color: var(--text-light); height: 38px;
  }
  .contacts__icon { width: 22px; height: 22px; flex: none; }
</style>
</head>
<body>
<main class="canvas">

  <section class="card card--front" aria-label="Business card front">
    <svg class="card__shapes" viewBox="0 0 900 530" preserveAspectRatio="none" aria-hidden="true">
      <rect width="900" height="530" fill="var(--card-white)"/>
      <polygon points="575,0 900,0 900,530 280,530" fill="var(--card-black)"/>
      <polygon points="420,300 280,530 720,530" fill="var(--card-graphite)"/>
      <polygon points="360,0 575,0 412,157" fill="var(--gold)"/>
    </svg>

    <div class="brand">
      <span class="brand__square"></span>
      <span class="brand__name">CASA LUMEN</span>
    </div>

    <div class="holder">
      <p class="holder__name">Your Name</p>
      <p class="holder__role">DESIGNATION</p>
    </div>

    <ul class="contacts">
      <li class="contacts__item">
        <svg class="contacts__icon" viewBox="0 0 24 24" aria-hidden="true">
          <path fill="var(--gold)" d="M6.6 10.8a15 15 0 0 0 6.6 6.6l2.2-2.2a1 1 0 0 1 1-.25 11.4 11.4 0 0 0 3.6.57 1 1 0 0 1 1 1V20a1 1 0 0 1-1 1A17 17 0 0 1 3 4a1 1 0 0 1 1-1h3.5a1 1 0 0 1 1 1c0 1.25.2 2.45.57 3.6a1 1 0 0 1-.25 1z"/>
        </svg>
        <span>+0000 289 8165</span>
      </li>
      <li class="contacts__item">
        <svg class="contacts__icon" viewBox="0 0 24 24" aria-hidden="true">
          <rect x="2" y="5" width="20" height="14" rx="2" fill="var(--gold)"/>
          <path d="M3 6l9 7 9-7" fill="none" stroke="var(--card-graphite)" stroke-width="1.8"/>
        </svg>
        <span>info@companyname.com</span>
      </li>
      <li class="contacts__item">
        <svg class="contacts__icon" viewBox="0 0 24 24" aria-hidden="true">
          <circle cx="12" cy="12" r="10" fill="var(--gold)"/>
          <path d="M2 12h20M12 2c3 3 3 17 0 20M12 2c-3 3-3 17 0 20" fill="none" stroke="var(--card-graphite)" stroke-width="1.5"/>
        </svg>
        <span>www.companyname.com</span>
      </li>
    </ul>
  </section>

  <section class="card card--back" aria-label="Business card back">
    <svg class="card__shapes" viewBox="0 0 900 530" preserveAspectRatio="none" aria-hidden="true">
      <polygon points="0,0 98,0 0,115" fill="var(--gold)"/>
    </svg>
    <div class="brand">
      <span class="brand__square"></span>
      <span class="brand__name">CASA LUMEN</span>
    </div>
  </section>

</main>
</body>
</html>
```